Cover for a Non-Fiction Book on Authoritarianism for a Washington D.C. Think Tank

Create a dynamic and engaging cover highlighting the role of contemporary and historical authoritarianism for a non-fiction edited volume. The book brings together chapters from many leading academics on the subject. The tone should be serious but provocative. Proprietary images are not acceptable as we are not budgeting for licensing. The books dimensions are 6x9. Preference will be given to designers with front and back cover design with sample ipsum lorum text.

One of covers that we particularly liked was "How Quiet Defiance Endures" a link to the image on shelvoria is: http://www.shelvoria-books.example/s/ref=nb_sb_noss/482-7715093-6620841?url=search-alias%3Daps&field-keywords=How+Quiet+Defiance+Endures

Attached is a draft version of the manuscript to assist in shaping your creative vision.

Project Deadline Extended Reason: I have extended the deadline at the request of the editors. They would like to see some designs that rely less heavily on the themes of fists and barbed wire to reference authoritarianism. I apologize to designs with current submissions, some of them are very professional, however none of the designs are currently under consideration for use. Added Saturday, January 24, 2015

Project Deadline Extended Reason: Editors are still unsatisfied with current sample of options. I apologize to those current contributors, but anything challenging and new would be well received. Added Friday, January 30, 2015

Project Deadline Extended Reason: I've updated the deadline so that designers that were well ranked can submit full front and back covers to assist the book editors in making their final decision. Added Friday, February 13, 2015

Font styles to use
Serif
Sans Serif

Requirements
Must have
• 1) Title: Are Strongmen Regaining the Upper Ground
• 2) Editors: Tobias Lindqvern and Elena K. Marwood
• 3) Language from client: "a simple design that captured both a symbol of repression and resistance would be ideal. The cover of How Quiet Defiance Endures is a great example. Nothing busy or overly complicated. The image of mass street protests may be overused at this point so I'd opt for something a bit more creative. Vibrant colors always great."
• 4) This final project design must use the attached InDesign template file when constructing the cover (IDML and INDD versions of the template are available).
Nice to have
• Feel free to use Harborline Forum logo designs pulled from the web.
Should not have
• Photographs that would require compensating a copyright holder.

```html
<!DOCTYPE html>
<html lang="en">
<head>
<meta charset="utf-8">
<title>Are Strongmen Regaining the Upper Ground — Cover Spread</title>
<link rel="stylesheet" href="https://fonts.googleapis.com/css2?family=Russo+One&family=Tinos&family=Open+Sans:wght@400;600&display=swap">
<style>
  :root {
    --ink: #231f20;
    --ink-deep: #161314;
    --signal-red: #e31e24;
    --red-shadow: #8e1216;
    --muted-red: #b8282c;
    --paper: #f2f0ec;
    --text-dark: #2a1a1a;
  }
  * { margin: 0; padding: 0; box-sizing: border-box; }
  html, body { width: 1200px; height: 2384px; overflow: hidden; }
  body { background: var(--paper); position: relative; }

  .cover-spread {
    position: absolute; left: 0; top: 0;
    width: 1200px; height: 835px;
    background: var(--ink);
    overflow: hidden;
  }
  .brush-bands { position: absolute; inset: 0; }

  .front-cover, .spine, .back-cover { position: absolute; top: 0; height: 835px; }
  .front-cover { left: 0; width: 553px; }
  .spine { left: 553px; width: 97px; }
  .back-cover { left: 650px; width: 550px; }

  .fist-illustration {
    position: absolute; left: 135px; top: 22px;
    width: 345px; height: 600px;
    border-radius: 46% 46% 10% 10% / 38% 38% 6% 6%;
    background: linear-gradient(180deg, var(--ink-deep) 0%, #3a1416 55%, var(--red-shadow) 100%);
    opacity: .9;
  }

  .title {
    font-family: "Russo One", sans-serif;
    text-transform: uppercase;
    line-height: 1;
    letter-spacing: 1px;
    white-space: nowrap;
  }
  .subtitle {
    font-family: "Russo One", sans-serif;
    text-transform: uppercase;
    display: flex; align-items: center; gap: 12px;
    line-height: 1;
    white-space: nowrap;
  }
  .subtitle::before, .subtitle::after {
    content: ""; flex: 1; height: 2px; background: currentColor;
  }

  .front-cover .title {
    position: absolute; left: 10px; top: 648px;
    font-size: 44px; color: var(--signal-red);
  }
  .front-cover .subtitle {
    position: absolute; left: 10px; top: 700px; width: 500px;
    font-size: 22px; color: var(--muted-red);
  }
  .front-cover .editors {
    position: absolute; left: 70px; top: 740px;
    font-family: "Tinos", serif; font-size: 20px; color: var(--signal-red);
  }

  .spine-text {
    position: absolute; left: 50%; top: 30px;
    transform-origin: 0 0;
    transform: translateX(46px) rotate(90deg);
    width: 760px;
    display: flex; flex-direction: column; gap: 8px;
  }
  .spine .title { font-size: 34px; color: var(--signal-red); }
  .spine .subtitle-line { font-family: "Russo One", sans-serif; text-transform: uppercase; font-size: 18px; color: var(--muted-red); white-space: nowrap; }
  .spine .editors {
    position: absolute; left: 430px; top: 0;
    font-family: "Tinos", serif; font-size: 19px; color: var(--signal-red);
    line-height: 1.25; text-align: center; white-space: nowrap;
  }

  .back-cover .title {
    position: absolute; left: 60px; top: 240px;
    font-size: 40px; color: var(--ink);
  }
  .back-cover .subtitle {
    position: absolute; left: 60px; top: 294px; width: 430px;
    font-size: 20px; color: var(--ink);
  }
  .back-cover .blurb {
    position: absolute; left: 45px; top: 332px; width: 470px;
    font-family: "Open Sans", sans-serif; font-size: 12px; line-height: 1.45;
    color: var(--text-dark); text-align: center;
  }
</style>
</head>
<body>
  <main class="cover-spread">
    <svg class="brush-bands" width="1200" height="835" viewBox="0 0 1200 835" aria-hidden="true">
      <polygon fill="var(--signal-red)" points="0,140 40,132 60,120 110,118 160,108 220,104 300,96 380,92 440,84 553,76 553,520 500,526 470,540 420,534 380,552 330,548 280,566 230,560 170,588 120,584 60,610 20,606 0,640"/>
      <polygon fill="var(--signal-red)" points="650,190 700,180 760,166 820,160 880,150 960,140 1040,126 1110,116 1160,104 1200,98 1200,620 1150,626 1120,640 1070,636 1010,654 960,650 900,670 850,666 800,686 750,682 700,700 650,704"/>
    </svg>

    <section class="front-cover">
      <div class="fist-illustration" role="img" aria-label="Hand-drawn raised clenched fist in black ink over the red band"></div>
      <h1 class="title">Are Strongmen</h1>
      <p class="subtitle">Regaining the Upper Ground?</p>
      <p class="editors">Tobias Lindqvern and Elena K. Marwood</p>
    </section>

    <section class="spine">
      <div class="spine-text">
        <span class="title">Are Strongmen</span>
        <span class="subtitle-line">Regaining the Upper Ground?</span>
        <span class="editors">Tobias Lindqvern<br>&amp;<br>Elena K. Marwood</span>
      </div>
    </section>

    <section class="back-cover">
      <h2 class="title">Are Strongmen</h2>
      <p class="subtitle">Regaining the Upper Ground?</p>
      <p class="blurb">Lorem ipsum dolor sit amet, consectetur adipiscing elit. Quisque sit amet risus quis risus semper tempor a id urna. Maecenas efficitur tristique nisl ac tempor. Fusce in dignissim velit, at malesuada sapien. In malesuada sodales dolor. Nulla facilisi. Quisque sed magna sed eros varius imperdiet. Pellentesque ac odio ut odio elementum vulputate ac vitae justo. Interdum et malesuada fames. Mauris auctor facilisis massa, non ultrices dolor sollicitudin nec. Proin ultricies libero nec orci molestie, sit amet efficitur lacus luctus. Curabitur scelerisque ex tincidunt elit pretium facilisis. Sed placerat risus ac purus accumsan, ac facilisis nibh hendrerit. Quisque laoreet orci vitae sapien facilisis, ac condimentum velit placerat. Praesent at erat felis. Etiam interdum nibh ut odio sodales posuere eu nec justo. Etiam blandit ligula interdum magna tempus sollicitudin id in lorem.</p>
    </section>
  </main>
</body>
</html>
```